Our business is a Startup that Employs Caregivers to do IN HOME Care of the Elderly. Our website is not yet running. But, a business similar to ours is info@brightlarkcare.com

We are looking for a card that only has 4 Elements:
-Logo
- Website
- Tag Line
- Phone
We would like to see some eye catching backgrounds.
We would like to see some designs with and some without a Photo.
Would like the Photo to be of a Caregiver taking care of a Senior. The photo should show both of them smiling.

Target Market(s)

Age 35-55 who has Parents that are Elderly and need care

Industry/Entity Type

Home Health Care

Contact Information for Business Card

Want it to Pop Out to the viewer . Thinking maybe:
Side 1: LOGO with Website & Tag line
Side 2: Phone Number

Font styles to use
Other font styles liked:
• Same Font as our Logo

Colors

Designer to choose colors to be used in the design.

Requirements
Must have
• Logo, website, Tag Line, Phone number and Email: "info@brightlarkcare.com"
• Please use one of the photos that I have attached.
Nice to have
• Would like to see a Photo worked in that has a Care Taker taking care of an Elderly Person and they are both smiling.

```html
<!DOCTYPE html>
<html lang="en">
<head>
<meta charset="utf-8">
<title>BrightlarkCare.com – Business Card</title>
<link rel="stylesheet" href="https://fonts.googleapis.com/css2?family=Nunito:wght@800&family=Roboto:ital,wght@0,400;0,500;1,700&display=swap">
<style>
  :root{
    --stage:#d6d6d6;
    --brand-blue:#0a56a6;
    --brand-orange:#f05a22;
    --card-white:#ffffff;
    --pattern-light:#ededed;
    --pattern-dark:#111111;
    --ink-white:#ffffff;
  }
  *{margin:0;padding:0;box-sizing:border-box}
  html,body{width:1200px;height:915px;overflow:hidden}
  body{
    background:var(--stage);
    display:flex;align-items:center;justify-content:center;gap:44px;
    font-family:"Roboto",Arial,sans-serif;
  }
  .card{
    position:relative;width:530px;height:303px;overflow:hidden;
    box-shadow:0 10px 24px rgba(0,0,0,.22);
  }
  .card__texture{position:absolute;inset:0}
  .card--front .card__texture{background:linear-gradient(135deg,#fafafa 0%,var(--pattern-light) 50%,#fbfbfb 100%)}
  .card--back .card__texture{background:linear-gradient(135deg,#1c1c1c 0%,var(--pattern-dark) 50%,#222 100%)}

  /* front */
  .front__shapes{position:absolute;inset:0}
  .front__info{position:absolute;left:34px;top:72px;color:var(--ink-white)}
  .brand-name{font-family:"Nunito",Arial,sans-serif;font-weight:800;line-height:1}
  .front__info .brand-name{font-size:24px;color:var(--ink-white)}
  .tagline{font-family:"Roboto",Arial,sans-serif;font-style:italic;font-weight:700}
  .front__info .tagline{font-size:11px;margin:4px 0 8px 2px}
  .contact{display:flex;align-items:center;gap:7px;font-size:14px;line-height:16px;margin-top:3px}
  .contact svg{width:14px;height:14px;flex:none}
  .front__mark{position:absolute;left:352px;top:118px;width:104px;height:104px;border-radius:50%;background:var(--brand-orange)}

  /* back */
  .back__band{
    position:absolute;left:0;right:0;top:88px;height:128px;background:var(--card-white);
  }
  .back__rule{position:absolute;left:0;right:0;height:3px;background:var(--brand-orange)}
  .back__rule--top{top:80px}
  .back__rule--bottom{top:221px}
  .back__lockup{
    position:absolute;left:0;right:0;top:88px;height:128px;
    display:flex;align-items:center;justify-content:center;gap:12px;
  }
  .back__mark{width:46px;height:46px;border-radius:50%;background:var(--brand-orange)}
  .back__lockup .brand-name{font-size:28px;color:var(--brand-blue)}
  .back__lockup .tagline{font-size:12px;color:var(--brand-blue);margin-top:4px;padding-left:2px}
</style>
</head>
<body>

  <section class="card card--front" aria-label="Card front">
    <div class="card__texture" role="img" aria-label="Light embossed diamond texture"></div>
    <svg class="front__shapes" viewBox="0 0 530 303" aria-hidden="true">
      <polygon points="0,42 88,42 100,54 100,60 0,60" fill="var(--brand-orange)"/>
      <polygon points="0,60 96,60 108,48 118,48 118,60 372,60 404,170 0,170" fill="var(--brand-blue)"/>
    </svg>
    <div class="front__info">
      <div class="brand-name">BrightlarkCare.com</div>
      <div class="tagline">Senior Care - Family Style</div>
      <div class="contact">
        <svg viewBox="0 0 14 14"><circle cx="7" cy="7" r="7" fill="#fff"/><path d="M4.6 3.6l1.3-.2.7 1.8-.9.7c.4.9 1 1.5 1.9 1.9l.7-.9 1.8.7-.2 1.3c-3 .3-5.6-2.3-5.3-5.3z" fill="var(--brand-blue)"/></svg>
        <span>(555) 555 5555</span>
      </div>
      <div class="contact">
        <svg viewBox="0 0 14 14"><circle cx="7" cy="7" r="7" fill="#fff"/><rect x="3.5" y="4.5" width="7" height="5" fill="none" stroke="var(--brand-blue)" stroke-width="1"/><path d="M3.5 4.5L7 7.4l3.5-2.9" fill="none" stroke="var(--brand-blue)" stroke-width="1"/></svg>
        <span>info@brightlarkcare.com</span>
      </div>
    </div>
    <div class="front__mark"></div>
  </section>

  <section class="card card--back" aria-label="Card back">
    <div class="card__texture" role="img" aria-label="Dark embossed diamond texture"></div>
    <div class="back__rule back__rule--top"></div>
    <div class="back__band"></div>
    <div class="back__rule back__rule--bottom"></div>
    <div class="back__lockup">
      <div class="back__mark"></div>
      <div>
        <div class="brand-name">BrightlarkCare.com</div>
        <div class="tagline">Senior Care - Family Style</div>
      </div>
    </div>
  </section>

</body>
</html>
```